Tri-Fold Brochure for Transportation Equipment Dealer

We need a design of a new tri-fold brochure for our company. This is what we give to customers and prospective customers. Many of our customers do not know the diversity of our product line and capabilities. We have a lot of information to share with them in a small package. I have provided a draft of the content that I wanted included (in a .pptx and .pdf format), but we need it enhanced with color and made to look more professional. We need it to be informative yet professional.

Target Market(s)

Transportation industry customers. Fleet carriers and owner/operator truck drivers.

Industry/Entity Type

Truck Service

Font styles to use
Serif
Sans Serif

Colors
3176b5

Requirements
Must have
• Color. Must include the information that I have provided in the draft. Must be US Letter size.
Nice to have
• Color and separation of different sections.

```html
<!DOCTYPE html>
<html lang="en">
<head>
<meta charset="utf-8">
<title>Tri-Fold Brochure – Inside Spread</title>
<link href="https://fonts.googleapis.com/css2?family=Oswald:wght@400;500;600&family=Open+Sans:wght@400;600;700&display=swap" rel="stylesheet">
<style>
  :root{
    --navy:#0d3566;
    --blue:#1c5aa2;
    --brand:#3176b5;
    --sky:#45a3ea;
    --panel:#eeeff1;
    --panel-dark:#d9dadd;
    --strip:#8b8d91;
    --ink:#222428;
    --muted:#55585e;
    --gold:#e2b21c;
    --red:#c8202b;
    --stage:#5f6265;
  }
  *{box-sizing:border-box;margin:0;padding:0}
  html,body{width:1200px;height:1200px;overflow:hidden;background:var(--stage)}
  .brochure{position:absolute;left:30px;top:160px;width:1140px;height:880px;background:var(--panel);box-shadow:0 20px 50px rgba(0,0,0,.35);font-family:"Open Sans",Arial,sans-serif;color:var(--ink)}
  .panel{position:absolute;top:0;width:380px;height:880px;overflow:hidden}
  .panel--blowers{left:0}
  .panel--trailers{left:380px;border-left:1px solid #cfd0d3}
  .panel--parts{left:760px;border-left:1px solid #cfd0d3}
  .section-band{position:absolute;left:0;top:0;width:100%;height:50px;background:var(--blue)}
  .section-tab{position:absolute;left:0;top:0;height:50px;padding:0 22px;background:var(--navy);font-family:"Oswald",sans-serif;font-size:20px;line-height:50px;color:var(--sky);letter-spacing:.5px}
  .foot-band{position:absolute;left:0;bottom:0;width:100%;height:22px;background:var(--blue)}
  .heading{font-family:"Oswald",sans-serif;font-weight:500;text-transform:uppercase;color:var(--ink)}
  .placeholder{background:linear-gradient(135deg,#b9bcc2,#7d828a)}

  /* Blowers */
  .blowers-title{position:absolute;left:24px;top:62px;font-size:21px}
  .awards{position:absolute;left:24px;top:98px;width:330px;display:flex;justify-content:space-between;border-bottom:2px solid var(--brand);padding-bottom:8px}
  .award{display:flex;flex-direction:column;align-items:center;font-family:"Oswald",sans-serif;font-size:12px}
  .award-icon{width:44px;height:48px;margin-bottom:4px}
  .brand-strip{position:absolute;left:0;top:186px;width:100%;height:72px;background:var(--panel-dark)}
  .brand-name{position:absolute;left:28px;top:18px;font-family:"Oswald",sans-serif;font-weight:600;font-size:28px;color:var(--ink)}
  .brand-mark{display:inline-block;width:12px;height:12px;background:var(--red);margin-right:8px;vertical-align:middle}
  .blower-photo{position:absolute;right:26px;top:5px;width:96px;height:62px;border-radius:12px;background:linear-gradient(135deg,#b3303c,#6e121b)}
  .blowers-copy{position:absolute;left:24px;top:274px;width:336px;font-size:11px;line-height:1.45;color:var(--muted)}
  .blowers-copy p{margin-bottom:10px;text-align:justify}
  .service-grid{position:absolute;left:24px;top:488px;width:336px;height:350px;border:1px solid #c4c6ca;border-radius:8px;display:grid;grid-template-columns:1fr 1fr;grid-template-rows:1fr 1fr;background:#f7f7f8}
  .service{border:1px solid #d8d9dc;display:flex;flex-direction:column;align-items:center;justify-content:center;gap:10px}
  .service-photo{width:130px;height:88px;border-radius:50%;border:4px solid var(--blue)}
  .service-photo--stock{background:linear-gradient(135deg,#9aa6b6,#3d4a5e)}
  .service-photo--repair{background:linear-gradient(135deg,#c5a98a,#4a5a6c)}
  .service-photo--pto{background:linear-gradient(135deg,#d6d3cd,#6b5b45)}
  .service-photo--package{background:linear-gradient(135deg,#9fb0c2,#4b5866)}
  .service-label{font-family:"Oswald",sans-serif;font-size:12px;text-transform:uppercase}

  /* Trailers */
  .trailer-list{position:absolute;left:16px;top:62px;width:254px}
  .trailer{position:relative;height:108px}
  .trailer-photo{position:absolute;left:0;top:6px;width:180px;height:58px;border-radius:4px}
  .trailer-label{position:absolute;right:0;top:66px;font-family:"Oswald",sans-serif;font-size:11px;line-height:14px;text-transform:uppercase}
  .trailer-rule{position:absolute;left:0;top:82px;width:254px;height:8px}
  .trailer-url{position:absolute;left:40px;top:90px;font-size:10.5px;line-height:14px;color:var(--brand)}
  .stock-strip{position:absolute;left:272px;top:50px;width:108px;height:672px;background:var(--strip)}
  .stock-text{position:absolute;left:54px;top:336px;width:620px;transform:translate(-50%,-50%) rotate(-90deg);text-align:center}
  .stock-heading{font-family:"Oswald",sans-serif;font-size:16px;color:#fff;text-transform:uppercase}
  .stock-url{font-size:11px;font-weight:700;color:var(--ink);margin-top:2px}
  .stock-rule{width:300px;height:1px;background:#fff;margin:8px auto}
  .stock-note{font-size:11px;color:#2e3034;line-height:1.4}
  .represent-band{position:absolute;left:0;top:722px;width:100%;height:44px;background:var(--navy)}
  .represent-label{position:absolute;left:22px;top:0;font-family:"Oswald",sans-serif;font-size:20px;line-height:44px;color:var(--sky)}
  .partners{position:absolute;left:0;top:766px;width:100%;height:92px;background:#fff;display:flex;align-items:center;justify-content:space-around;padding:0 10px}
  .partner{font-family:"Oswald",sans-serif;font-size:15px;font-weight:500;color:var(--navy);display:flex;align-items:center;gap:5px}
  .partner-dot{width:9px;height:9px;background:var(--navy)}
  .partner-badge{width:30px;height:30px;background:#9aa0a8}
  .partner-more{font-family:"Oswald",sans-serif;font-size:12px;color:var(--red)}

  /* Parts */
  .parts-headline{position:absolute;left:22px;top:62px;width:336px;font-size:19px;line-height:1.15}
  .parts-grid{position:absolute;left:18px;top:122px;width:344px;display:grid;grid-template-columns:repeat(3,1fr);row-gap:0}
  .part{height:138px;border-bottom:1.5px dashed #7a7d83;display:flex;flex-direction:column;align-items:center;justify-content:center;gap:8px}
  .part-photo{width:88px;height:78px;border-radius:8px}
  .part-photo--kit{background:linear-gradient(135deg,#444,#111)}
  .part-photo--cover{background:linear-gradient(135deg,#c8cacd,#6f7276)}
  .part-photo--valve{background:linear-gradient(135deg,#6d6e70,#1c1c1d)}
  .part-photo--bar{background:linear-gradient(135deg,#e4e5e7,#9ea2a7)}
  .part-photo--pto{background:linear-gradient(135deg,#d23a3a,#555)}
  .part-photo--fit{background:linear-gradient(135deg,#d9b35a,#8b95a1)}
  .part-photo--cam{background:linear-gradient(135deg,#8a8d92,#3d4046)}
  .part-photo--pump{background:linear-gradient(135deg,#3a5aa8,#1a2550)}
  .part-photo--filter{background:linear-gradient(135deg,#d8dde2,#6e8090)}
  .part-label{font-family:"Oswald",sans-serif;font-size:11px;text-align:center}
  .warehouse-photo{position:absolute;left:0;top:540px;width:100%;height:318px;background:linear-gradient(160deg,#6d6e70 0%,#3a3634 55%,#1e1c1b 100%)}
</style>
</head>
<body>
<main class="brochure">

  <section class="panel panel--blowers">
    <div class="section-band"></div>
    <div class="section-tab">BLOWERS</div>
    <h2 class="heading blowers-title">#1 USA Mobile Blower Distributor</h2>
    <div class="awards">
      <div class="award"><svg class="award-icon" viewBox="0 0 44 48" role="img" aria-label="Award trophy"><path d="M10 4h24v12a12 12 0 0 1-24 0z" fill="var(--gold)"/><rect x="19" y="28" width="6" height="8" fill="var(--gold)"/><rect x="12" y="36" width="20" height="6" fill="var(--gold)"/></svg>2014</div>
      <div class="award"><svg class="award-icon" viewBox="0 0 44 48" role="img" aria-label="Award trophy"><path d="M10 4h24v12a12 12 0 0 1-24 0z" fill="var(--gold)"/><rect x="19" y="28" width="6" height="8" fill="var(--gold)"/><rect x="12" y="36" width="20" height="6" fill="var(--gold)"/></svg>2015</div>
      <div class="award"><svg class="award-icon" viewBox="0 0 44 48" role="img" aria-label="Award trophy"><path d="M10 4h24v12a12 12 0 0 1-24 0z" fill="var(--gold)"/><rect x="19" y="28" width="6" height="8" fill="var(--gold)"/><rect x="12" y="36" width="20" height="6" fill="var(--gold)"/></svg>2016</div>
      <div class="award"><svg class="award-icon" viewBox="0 0 44 48" role="img" aria-label="Award trophy"><path d="M10 4h24v12a12 12 0 0 1-24 0z" fill="var(--gold)"/><rect x="19" y="28" width="6" height="8" fill="var(--gold)"/><rect x="12" y="36" width="20" height="6" fill="var(--gold)"/></svg>2017</div>
    </div>
    <div class="brand-strip">
      <div class="brand-name"><span class="brand-mark"></span>Kestrel Air</div>
      <div class="blower-photo" role="img" aria-label="Red mobile blower unit"></div>
    </div>
    <div class="blowers-copy">
      <p>We are proud to represent the Kestrel Air line of mobile products for use in dry bulk liquid and hydraulic applications. Kestrel Air blowers are the most efficient and productive blowers on the market.</p>
      <p>We specialize in blower installations for your trailer or truck. With our expertise and several model designs we can meet any mounting arrangement or need.</p>
      <p>We can integrate your system with hydraulics as well as power take off units (PTO).</p>
    </div>
    <div class="service-grid">
      <div class="service"><div class="service-photo service-photo--stock" role="img" aria-label="Blowers in stock on warehouse floor"></div><span class="service-label">Stock</span></div>
      <div class="service"><div class="service-photo service-photo--repair" role="img" aria-label="Technician repairing a blower"></div><span class="service-label">Repair</span></div>
      <div class="service"><div class="service-photo service-photo--pto" role="img" aria-label="PTO kit components"></div><span class="service-label">PTO Kits</span></div>
      <div class="service"><div class="service-photo service-photo--package" role="img" aria-label="Assembled blower package unit"></div><span class="service-label">Package Units</span></div>
    </div>
    <div class="foot-band"></div>
  </section>

  <section class="panel panel--trailers">
    <div class="section-band"></div>
    <div class="section-tab">TRAILERS</div>
    <div class="trailer-list">
      <div class="trailer"><div class="trailer-photo placeholder" role="img" aria-label="Stainless vacuum pneumatic tank trailer"></div><span class="trailer-label">Vacuum Pneumatic</span><svg class="trailer-rule" viewBox="0 0 254 8"><line x1="0" y1="4" x2="248" y2="4" stroke="var(--blue)" stroke-width="1.5"/><path d="M246 0l8 4-8 4z" fill="var(--blue)"/></svg></div>
      <div class="trailer"><div class="trailer-photo placeholder" role="img" aria-label="Aluminum hopper trailer"></div><span class="trailer-label">Hopper</span><svg class="trailer-rule" viewBox="0 0 254 8"><line x1="0" y1="4" x2="248" y2="4" stroke="var(--blue)" stroke-width="1.5"/><path d="M246 0l8 4-8 4z" fill="var(--blue)"/></svg></div>
      <div class="trailer"><div class="trailer-photo placeholder" role="img" aria-label="Dry bulk pneumatic trailer"></div><span class="trailer-label">Dry Bulk Pneumatic</span><svg class="trailer-rule" viewBox="0 0 254 8"><line x1="0" y1="4" x2="248" y2="4" stroke="var(--blue)" stroke-width="1.5"/><path d="M246 0l8 4-8 4z" fill="var(--blue)"/></svg></div>
      <div class="trailer"><div class="trailer-photo" style="background:linear-gradient(135deg,#555,#111)" role="img" aria-label="Black lowboy trailer"></div><span class="trailer-label">Lowboys</span><svg class="trailer-rule" viewBox="0 0 254 8"><line x1="0" y1="4" x2="248" y2="4" stroke="var(--blue)" stroke-width="1.5"/><path d="M246 0l8 4-8 4z" fill="var(--blue)"/></svg><span class="trailer-url">www.primelowbeds.com</span></div>
      <div class="trailer"><div class="trailer-photo placeholder" role="img" aria-label="End dump trailer"></div><span class="trailer-label">End Dump</span><svg class="trailer-rule" viewBox="0 0 254 8"><line x1="0" y1="4" x2="248" y2="4" stroke="var(--blue)" stroke-width="1.5"/><path d="M246 0l8 4-8 4z" fill="var(--blue)"/></svg></div>
      <div class="trailer"><div class="trailer-photo placeholder" role="img" aria-label="Belt trailer"></div><span class="trailer-label">Belt</span><svg class="trailer-rule" viewBox="0 0 254 8"><line x1="0" y1="4" x2="248" y2="4" stroke="var(--blue)" stroke-width="1.5"/><path d="M246 0l8 4-8 4z" fill="var(--blue)"/></svg></div>
    </div>
    <div class="stock-strip">
      <div class="stock-text">
        <div class="stock-heading">Check out our current stock and inventory at:</div>
        <div class="stock-url">www.haulwayequip.com/inventory</div>
        <div class="stock-rule"></div>
        <div class="stock-note">We can custom configure your trailer to meet your requirements<br>We have the ability to do aftermarket modifications to your specs</div>
      </div>
    </div>
    <div class="represent-band"><span class="represent-label">REPRESENTING</span></div>
    <div class="partners">
      <span class="partner"><span class="partner-dot"></span>Ridgeway</span>
      <span class="partner">Velmora</span>
      <span class="partner">Brantley</span>
      <span class="partner-badge" role="img" aria-label="Partner badge"></span>
      <span class="partner">Corvan</span>
      <span class="partner-more">+MORE!</span>
    </div>
    <div class="foot-band"></div>
  </section>

  <section class="panel panel--parts">
    <div class="section-band"></div>
    <div class="section-tab">PARTS</div>
    <h2 class="heading parts-headline">99% of parts in stock ship within 24 hours of receipt of order</h2>
    <div class="parts-grid">
      <div class="part"><div class="part-photo part-photo--kit" role="img" aria-label="Hydraulic and wet line kit"></div><span class="part-label">Hydraulic &amp; Wet Line Kits</span></div>
      <div class="part"><div class="part-photo part-photo--cover" role="img" aria-label="Manhole cover trailer part"></div><span class="part-label">Trailer Parts</span></div>
      <div class="part"><div class="part-photo part-photo--valve" role="img" aria-label="Valve with gasket rings"></div><span class="part-label">Valves &amp; Fittings</span></div>
      <div class="part"><div class="part-photo part-photo--bar" role="img" aria-label="Trailer manifold bar"></div><span class="part-label">Trailer Parts</span></div>
      <div class="part"><div class="part-photo part-photo--pto" role="img" aria-label="PTO unit"></div><span class="part-label">PTO</span></div>
      <div class="part"><div class="part-photo part-photo--fit" role="img" aria-label="Brass and steel fittings"></div><span class="part-label">Hose &amp; Fittings</span></div>
      <div class="part"><div class="part-photo part-photo--cam" role="img" aria-label="Cam lock couplings"></div><span class="part-label">Hose &amp; Fittings</span></div>
      <div class="part"><div class="part-photo part-photo--pump" role="img" aria-label="Vacuum pump"></div><span class="part-label">Vacuum Pump</span></div>
      <div class="part"><div class="part-photo part-photo--filter" role="img" aria-label="Filter and precleaner"></div><span class="part-label">Filter &amp; Precleaner</span></div>
    </div>
    <div class="warehouse-photo" role="img" aria-label="Parts warehouse with stocked shelving"></div>
    <div class="foot-band"></div>
  </section>

</main>
</body>
</html>
```